Business Card Design

I need a business card for my rental business. The business is named:
Hire a Vorlatrike Brenmoor
www.hireavorlatrikebrenmoor.example
(555) 014-2937
This will be a business card that I will leave at other businesses as advertisement so it needs to have the name, website, and phone number.
Please feel free to be creative. This is a new business so I have no designs.
Thank you very much for your time and I look forward to receiving your designs
Target Market(s)
Local rental customers
Industry/Entity Type
Business
Contact Information for Business Card
Please check out my website:
Other font styles liked:
- anything creative
Colors
Designer to choose colors to be used in the design.
Requirements
Must have
- Business name, phone, website. Rentals available hourly or daily. Book online

```html
<!DOCTYPE html>
<html lang="en">
<head>
<meta charset="utf-8">
<title>Hire a Vorlatrike Brenmoor — Business Card</title>
<link rel="stylesheet" href="https://fonts.googleapis.com/css2?family=Exo+2:ital,wght@1,800&family=Lato:wght@400&display=swap">
<style>
  :root {
    --backdrop: #2b2b2b;
    --card: #1f1f1f;
    --card-edge: #272727;
    --name-front: #bdbdbd;
    --name-back: #8c8c8c;
    --muted: #6f6f6f;
    --contact: #cfcfcf;
    --rule: #8a8a8a;
  }
  * { box-sizing: border-box; margin: 0; padding: 0; }
  html, body {
    width: 1200px;
    height: 716px;
    overflow: hidden;
    background: var(--backdrop);
  }
  .sheet {
    width: 1200px;
    height: 716px;
    display: flex;
    align-items: center;
    justify-content: center;
    gap: 40px;
  }
  .card {
    position: relative;
    width: 520px;
    height: 300px;
    border-radius: 6px;
    background: linear-gradient(135deg, var(--card-edge), var(--card));
    box-shadow: 0 10px 28px rgba(0, 0, 0, 0.45);
  }
  .brand-name {
    font-family: "Exo 2", sans-serif;
    font-style: italic;
    font-weight: 800;
    text-transform: uppercase;
    letter-spacing: 0.3px;
    white-space: nowrap;
    line-height: 1.1;
  }
  /* Front side */
  .card-front .brand-block {
    position: absolute;
    right: 60px;
    top: 50%;
    transform: translateY(-50%);
    text-align: right;
  }
  .card-front .brand-name {
    font-size: 23px;
    color: var(--name-front);
  }
  .card-front .web {
    margin-top: 6px;
    font-family: "Lato", sans-serif;
    font-size: 11px;
    color: var(--muted);
  }
  /* Back side */
  .card-back .brand-name {
    position: absolute;
    left: 36px;
    top: 40px;
    font-size: 26px;
    color: var(--name-back);
  }
  .card-back .rule {
    position: absolute;
    left: 36px;
    top: 94px;
    width: 120px;
    height: 1px;
    background: var(--rule);
  }
  .contact-list {
    position: absolute;
    left: 36px;
    bottom: 40px;
    list-style: none;
    font-family: "Lato", sans-serif;
    font-size: 14px;
    color: var(--contact);
  }
  .contact-list li {
    display: flex;
    align-items: center;
    gap: 8px;
    margin-top: 8px;
  }
  .contact-list svg {
    width: 13px;
    height: 13px;
    flex: none;
  }
</style>
</head>
<body>
  <main class="sheet">
    <section class="card card-front">
      <div class="brand-block">
        <h1 class="brand-name">Hire a Vorlatrike Brenmoor</h1>
        <p class="web">www.hireavorlatrikebrenmoor.example</p>
      </div>
    </section>

    <section class="card card-back">
      <h2 class="brand-name">Hire a Vorlatrike Brenmoor</h2>
      <div class="rule"></div>
      <ul class="contact-list">
        <li>
          <svg viewBox="0 0 16 16" aria-hidden="true">
            <path d="M1 6c0-2 3-3.5 7-3.5S15 4 15 6v1.2h-3.5V5.8C10.8 5.4 9.5 5.2 8 5.2s-2.8.2-3.5.6v1.4H1z M3.5 8h9l1.5 6H2z" fill="var(--muted)"/>
            <circle cx="8" cy="11" r="1.6" fill="var(--card)"/>
          </svg>
          <span>(555) 014-2937</span>
        </li>
        <li>
          <svg viewBox="0 0 16 16" aria-hidden="true" fill="none" stroke="var(--muted)" stroke-width="1.2">
            <circle cx="8" cy="8" r="6.5"/>
            <ellipse cx="8" cy="8" rx="3" ry="6.5"/>
            <path d="M1.5 8h13M2.5 4.8h11M2.5 11.2h11"/>
          </svg>
          <span>www.hireavorlatrikebrenmoor.example</span>
        </li>
      </ul>
    </section>
  </main>
</body>
</html>
```